Design Briefpapier
Zielgruppe
Veranstaltungstechnik
Aufgabenstellung
Wir möchten unser Layout (Briefkopf, Header, Footer) neu gestalten lassen. Es existiert bereits ein Logo, das leicht verändert im Header erscheinen soll! WICHTIG: Das Logo soll schwarz hinterlegt werden auf dem Briefpapier, damit das eigentliche Design (orange auf schwarz) auch zur Geltung kommt.
Marke für hochwertige Trauerartikel benötigt Briefpapier Marke für hochwertige Trauerartikel benötigt Briefpapier"
Wir benötigen Briefpapier: Anschreiben, Rechnngsformular in Farbe und in schwarz weiß. Dazu Visitenkarten und ein gleicherscheinenden E-Mail Absender. Das Design sollte so klar wir möglich sein. Der Druck erfolgt auf recyceltem Papier.
Briefpapierbogen-/Visitenkarten-Design für KFZ-Unternehmen Briefpapierbogen-/Visitenkarten-Design für KFZ-Unternehmen"
Wir benötigen ein Briefpapierbogen sowie ein Visitenkarten Design! Folgende Angaben müssen auf dem Briefpapier sein: - Logo (siehe Anhang) - Anschrift (KW Solutions UG (haftungsbeschränkt), Tannweg 7, 75412 Borlingen - Wasserzeichen - GF (Jürgen Talkeni) - Bankverbindung ( IBAN DE42 8157 2290..
Briefpapier für Seehafenspedition im Bereich Zollabfertigung Briefpapier für Seehafenspedition im Bereich Zollabfertigung"
Wir bitten um ein Design für unser Briefpapier. Wir suchen ein hochwertiges Design, das die Werte Vertrauen, Exklusivität und Innovation ausstrahlt. Es soll edel aussehen. Bitte für Telefon, Mail etc. Icons benutzen, damit es für jedermann verständlich ist, unabhängig von der Sprach..
Geschäftspapiere für medizinische Schutzausrüstung Geschäftspapiere für medizinische Schutzausrüstung"
Es sollte clean sein, Farben wie , Weiß, blau, grün, wären von Vorteil. Habe keine besondere Vorstellungen lasse mich gerne überraschen. Siehe .. www.vaskoru.de
Geschäftspapiere für Rechtsanwaltskanzlei Geschäftspapiere für Rechtsanwaltskanzlei"
Bitte inklusive Logo (sollte Recht, Digital/Apps, Medizin illustrieren) - habe das Preisgeld vor diesem Hintergrund erhöht. ------------------------- Die Kanzlei arbeitet an der Schnittstelle von (Medizin-)Recht und Digital. Von daher wären wären Symbole/Gestaltung aus Bereich Medizin, Recht..

```html
<!DOCTYPE html>
<html lang="de">
<head>
<meta charset="utf-8">
<title>halvenkord – Briefpapier</title>
<link rel="stylesheet" href="https://fonts.googleapis.com/css2?family=Questrial&display=swap">
<style>
  :root {
    --stage: #b9bfc1;
    --paper: #ffffff;
    --navy: #182e37;
    --orange: #ef7d0b;
    --text: #1c2a33;
    --watermark: #eef0f1;
  }
  * { margin: 0; padding: 0; box-sizing: border-box; }
  html, body { width: 873px; height: 1200px; overflow: hidden; }
  body {
    position: relative;
    background: var(--stage);
    font-family: "Questrial", "Century Gothic", sans-serif;
    color: var(--text);
  }
  .sheet {
    position: absolute; left: 54px; top: 58px;
    width: 771px; height: 1091px;
    background: var(--paper);
  }
  .header-band {
    position: absolute; left: 75px; top: 42px;
    width: 671px; height: 70px;
    background: var(--navy);
    border-radius: 35px 0 0 35px;
  }
  .brand-dot {
    position: absolute; left: 18px; top: 20px;
    width: 30px; height: 30px; border-radius: 50%;
    background: var(--orange);
  }
  .brand-name {
    position: absolute; left: 62px; top: 14px;
    font-size: 34px; line-height: 40px; color: #fff;
    letter-spacing: 0.5px;
  }
  .header-accent {
    position: absolute; left: 746px; top: 42px;
    width: 25px; height: 70px; background: var(--orange);
  }
  .accent-rule {
    position: absolute; left: 746px; top: 112px;
    width: 1.5px; height: 156px; background: var(--orange);
  }
  .small { font-size: 9.6px; line-height: 11px; }
  .return-address { position: absolute; left: 91px; top: 182px; }
  .sender-block {
    position: absolute; right: 40px; top: 182px; text-align: right;
    font-style: normal;
  }
  .sender-block p + p { margin-top: 11px; }
  .web { color: var(--orange); font-weight: bold; }
  .fold-mark {
    position: absolute; left: 11px; width: 19px; height: 1px;
  }
  .fold-mark.top { top: 386px; background: var(--navy); }
  .fold-mark.punch { top: 545px; background: var(--orange); }
  .watermark {
    position: absolute; left: 322px; top: 544px;
  }
  .footer-col { position: absolute; top: 1012px; }
  .footer-col p + p { margin-top: 11px; }
  .col-bank { left: 91px; }
  .col-seat { left: 319px; }
  .col-partner { left: 541px; }
  .footer-rule {
    position: absolute; top: 1010px; width: 1.5px; height: 67px;
    background: var(--orange);
  }
</style>
</head>
<body>
  <main class="sheet">
    <header>
      <div class="header-band">
        <span class="brand-dot"></span>
        <div class="brand-name">halvenkord</div>
      </div>
      <div class="header-accent"></div>
      <div class="accent-rule"></div>
    </header>

    <div class="return-address small">halvenkord GmbH &amp; Co. KG &nbsp;· Lindauer Str. 14 &nbsp;· 10779 Berlin</div>

    <address class="sender-block small">
      <p>halvenkord GmbH &amp; Co. KG<br>Lindauer Str. 14 &nbsp;· 10779 Berlin</p>
      <p>Tel. 030 481 220 16<br>Fax. 030 481 220 17</p>
      <p>info@halvenkord-audio.de<br><span class="web">www.halvenkord-audio.de</span></p>
    </address>

    <span class="fold-mark top"></span>
    <span class="fold-mark punch"></span>

    <svg class="watermark" width="440" height="440" viewBox="0 0 440 440" aria-hidden="true">
      <circle cx="216" cy="216" r="214" fill="none" stroke="var(--watermark)" stroke-width="3"/>
    </svg>

    <footer>
      <div class="footer-col col-bank small">
        <p>Bankverbindung: Spreeland Bank<br>Konto: 072318840 &nbsp;· BLZ: 100 524 17</p>
        <p>IBAN: &nbsp;DE31 1005 2417 0072 3188 40<br>BIC / SWIFT: SPLB DE BB 210</p>
      </div>
      <span class="footer-rule" style="left:278px"></span>
      <div class="footer-col col-seat small">
        <p>Sitz der Gesellschaft: Berlin<br>Amtsgericht Berlin &nbsp;· HRA 47102</p>
        <p>Geschäftsführer:<br>Tobias Renkel, Marek Ostwald<br>USt-ID: DE318406275</p>
      </div>
      <span class="footer-rule" style="left:500px"></span>
      <div class="footer-col col-partner small">
        <p>Persönlich haftende Gesellschafterin:<br>halvenkord Verwaltungs-GmbH</p>
        <p>Geschäftsführer:<br>Tobias Renkel, Marek Ostwald<br>Amtsgericht Berlin &nbsp;· HRB 58213</p>
      </div>
      <span class="footer-rule" style="left:746px"></span>
    </footer>
  </main>
</body>
</html>
```